Counseling Practice Business Card

I need a professional looking business card incorporating my new logo that was just completed. Card needs to incorporate my name and title, description of my specialty, my address, my phone number, my fax number, my email and my website URL. I need to be able to choose design on/with different paper colors and textures.
I do not have a lot of business card ideas so I am open to anything but I want bold,sharp, clear card without additional designs other than my logo (see attached file info). I am open to different color backgrounds or paper colors including black. I do not like traditional brackets around area codes in phone number or dashes between numbers in phone number. Am open to other ways of presenting including periods between numbers as appropriate. I do not know enough to know what I like yet but I want card to coordinate and work together with my logo. My practice emphasizes natural mental health interventions so any use of color (with background paper color or the blue and green in my logo) that elicits nature is nice. In addition to black, any natural brown or wood looking background might be desirable also. Most of the offerings so far look very similar and boring.

Target Market(s)

Potential therapy clients and other professionals

Contact Information for Business Card

Card information:
Marcus T. Whitfield, Ph.D.
Licensed Clinical Psychologist
Integrative Health Coach
4812 Ferndale Pkwy NW
Suite 730
Cedarbrook, NC 27514
(919) 555-0142 phone
(919) 555-0186 fax
drmarcuswhitfield@kelvora.com
pathbloomcounseling.com

Font styles to use
Serif
Sans Serif
Other font styles liked:
• anything that you think looks crisp, clear and easily readable

Requirements
Must have
• Any color used should coordinate with my logo design (see attached files).
• Card should be printed horizontally so top and bottom are longest sides of rectangle.
• Background color or paper color should complement and highlight logo. Do not like a white background. black, grey, brown or any color my logo would blend well with.
Nice to have
• I would like designer to utilize color to highlight letters/name or phone-fax-web symbols.
• Bottom edge of card could be highlighted if appropriate to an idea.
Should not have
• I would NOT want the card to have a pure white background at all.
• No clear cards.
• Cards should be oriented with long sides on bottom and top, NOT sides. DO NOT LIKE THIS THIN TALL ORIENTATION.

```html
<!DOCTYPE html>
<html lang="en">
<head>
<meta charset="utf-8">
<title>Pathbloom Counseling – Business Card</title>
<link rel="stylesheet" href="https://fonts.googleapis.com/css2?family=Questrial&display=swap">
<style>
  :root {
    --bg: #5f6470;
    --paper: #f3f3f1;
    --green: #0f6b35;
    --blue: #2f6fb3;
    --ink: #4a4a4a;
  }
  * { margin: 0; padding: 0; box-sizing: border-box; }
  html, body { width: 1200px; height: 900px; overflow: hidden; }
  body {
    background: var(--bg);
    font-family: "Questrial", "Century Gothic", sans-serif;
    display: flex;
    flex-direction: column;
    align-items: center;
    justify-content: center;
    gap: 36px;
  }
  .card {
    position: relative;
    width: 700px;
    height: 400px;
    background: var(--paper);
    box-shadow: 0 10px 30px rgba(0,0,0,.35);
    display: flex;
    flex-direction: column;
    align-items: center;
    overflow: hidden;
  }
  .edge-band {
    position: absolute;
    left: 0; right: 0; bottom: 0;
    height: 12px;
    display: flex;
  }
  .edge-band .green { flex: 0 0 50%; background: var(--green); }
  .edge-band .blue  { flex: 1; background: var(--blue); border-left: 3px solid var(--paper); }

  .practice-name {
    color: var(--blue);
    font-size: 46px;
    font-weight: 400;
    line-height: 1;
    text-align: center;
  }

  /* back */
  .card-back { justify-content: center; padding-bottom: 20px; }
  .card-back .url {
    margin-top: 24px;
    color: var(--green);
    font-size: 17px;
    letter-spacing: 3px;
  }

  /* front */
  .card-front { padding-top: 52px; }
  .card-front .practice-name { font-size: 40px; }
  .person {
    margin-top: 38px;
    color: var(--green);
    font-size: 25px;
    font-weight: 700;
    letter-spacing: .5px;
  }
  .title { margin-top: 6px; color: var(--blue); font-size: 16px; }
  .contact {
    margin-top: 16px;
    color: var(--ink);
    font-size: 15px;
    text-align: center;
    line-height: 1.75;
  }
  .contact .item { display: inline-flex; align-items: center; gap: 6px; margin: 0 8px; }
  .contact svg { width: 13px; height: 13px; fill: var(--green); }
</style>
</head>
<body>

  <section class="card card-back">
    <div class="practice-name">Pathbloom Counseling</div>
    <div class="url">www.pathbloomcounseling.com</div>
    <div class="edge-band"><span class="green"></span><span class="blue"></span></div>
  </section>

  <section class="card card-front">
    <div class="practice-name">Pathbloom Counseling</div>
    <div class="person">Marcus T. Whitfield, Ph.D.</div>
    <div class="title">Licensed Clinical Psychologist | Integrative Health Coach</div>
    <div class="contact">
      <div>4812 Ferndale Pkwy NW, Suite 730, Cedarbrook, NC 27514</div>
      <div>
        <span class="item">
          <svg viewBox="0 0 16 16" aria-hidden="true"><path d="M3.6 1.2l2.3 2.3-1.3 1.9c.8 1.9 2.2 3.3 4.1 4.1l1.9-1.3 2.3 2.3-1.6 2.3C6.5 13 3 9.5 1.3 4.7z"/></svg>
          919.555.0142
        </span>
        <span class="item">
          <svg viewBox="0 0 16 16" aria-hidden="true"><path d="M4 1h7v4H4zM1 6h14v7h-3v2H4v-2H1zm4 5v3h6v-3z"/></svg>
          919.555.0186
        </span>
      </div>
      <div>
        <span class="item">
          <svg viewBox="0 0 16 16" aria-hidden="true"><path d="M1 3h14v10H1zm1.5 1.3L8 8.6l5.5-4.3z"/></svg>
          drmarcuswhitfield@kelvora.com
        </span>
        <span class="item">
          <svg viewBox="0 0 16 16" aria-hidden="true"><path d="M8 1a7 7 0 100 14A7 7 0 008 1zm0 1.5c.9 0 1.9 1.5 2.2 4H5.8C6.1 4 7.1 2.5 8 2.5zM2.6 6.5h1.7c.1-1.4.4-2.6.9-3.5a5.5 5.5 0 00-2.6 3.5zm0 3a5.5 5.5 0 002.6 3.5c-.5-.9-.8-2.1-.9-3.5zm3.2 0c.3 2.5 1.3 4 2.2 4s1.9-1.5 2.2-4zm5.9 0c-.1 1.4-.4 2.6-.9 3.5a5.5 5.5 0 002.6-3.5zm1.7-3A5.5 5.5 0 0010.8 3c.5.9.8 2.1.9 3.5z"/></svg>
          www.pathbloomcounseling.com
        </span>
      </div>
    </div>
    <div class="edge-band"><span class="green"></span><span class="blue"></span></div>
  </section>

</body>
</html>
```